Label or packaging Design for Hair Care Line

Dear Designer,
We are Corvella, a brand known for our premium hairstyling tools, and we are excited to expand into hair care. We are currently looking for a talented designer to create the label designs for our entire luxury hair care line.
This project is crucial in establishing our visual identity in the hair care market, and we aim to position ourselves alongside premium brands such as LTP, Dorvane Hair Atelier, and Pelmi.
Project Scope
We need a cohesive label design for our hair care line, which includes:
5 products (e.g., shampoo, conditioner, hair oil, styling cream, and a hair mask).
The designs should include:
Front label: Highlighting the product name, key features, and branding.
Our goal is to achieve a design that communicates premium luxury with a touch of professionalism. Below are the specific guidelines to help you align with our vision:
Style and Inspiration
Think of brands like LTP, Dorvane Hair Atelier, and Pelmi.
Luxury and Minimalism: Clean lines, sophisticated typography, and an elegant color palette.
Subtle femininity: premium finishes like metallic accents (gold, silver, or rose gold).
Brand Personality
Premium: Reflecting high quality and exclusivity.
Modern & Professional: Appealing to a refined, professional audience but also suitable for lifestyle-oriented customers.
Warm & Empowering: A brand that celebrates confidence and individuality.
Color Palette
Neutral tones like black, white, accented with metallics (gold or silver) for a luxurious feel.
Colors that feel timeless and elegant rather than trendy or overly bright.
Typography
Use clean, modern fonts (preferably sans-serif or serif for a refined look).
Clear and legible for all product details while maintaining a high-end aesthetic.
Materials and Finishes
Packaging Shape
The label designs should suit a variety of bottle and jar shapes (e.g., cylindrical, flat, or rounded).
Keep scalability in mind so the identity remains consistent across different products.
Deliverables
To understand the aesthetic we are aiming for, here are some brands to use as inspiration:
LTP: For its minimalistic and modern approach.
Dorvane Hair Atelier: For its combination of luxury and professional appeal.
Pelmi: For its soft femininity and lifestyle branding.
we would like to see your designs applied to a variety of packaging types to get an overall impression of how the brand identity works across different product formats. This includes:
A squeeze bottle (e.g., for styling creams or conditioners).
A glass bottle with a dropper (e.g., for a luxurious hair oil).
A shampoo/conditioner bottle (standard pump or flip-top cap).
A spray bottle (e.g., for leave-in treatments or heat protectors).
By creating designs for these different packaging types, we can better evaluate how cohesive and versatile the brand identity will be across the entire product line.

Updates
As you may have noticed from the designs, they don’t quite align with our briefing. The look needs to be clean and professional, similar to Dorvane, LTP, and the other examples we provided. Please address this, and we’ll check it!

Target Market(s)
europe and us
Font styles to use
Other font styles liked:
- century gothic

Look and feel
Each slider illustrates characteristics of the customer's brand and the style your logo design should communicate.

```html
<!DOCTYPE html>
<html lang="en">
<head>
<meta charset="utf-8">
<title>Corvella Hair Care Labels</title>
<link href="https://fonts.googleapis.com/css2?family=Poppins:wght@600&family=Questrial&display=swap" rel="stylesheet">
<style>
  :root {
    --page: #ffffff;
    --black: #151515;
    --charcoal: #2a2b2d;
    --sand: #d8d0bb;
    --sand-deep: #c2b797;
    --gold: #c9b58d;
    --white: #f2f2f2;
    --ink: #1c1c1c;
  }
  * { box-sizing: border-box; margin: 0; padding: 0; }
  html, body { width: 1200px; height: 1200px; overflow: hidden; background: var(--page); }
  .line-up {
    width: 1200px; height: 1200px;
    display: flex; align-items: flex-end; justify-content: center;
    gap: 24px; padding-bottom: 290px;
  }
  .label {
    display: flex; flex-direction: column; align-items: center;
    text-align: center; font-family: "Questrial", sans-serif;
    border-radius: 4px;
  }
  .label--dark { background: linear-gradient(90deg, var(--black), var(--charcoal) 45%, var(--black)); color: var(--white); }
  .label--light { background: linear-gradient(90deg, var(--sand-deep), var(--sand) 45%, var(--sand-deep)); color: var(--ink); }
  .product-name { font-family: "Poppins", sans-serif; font-weight: 600; line-height: 1.05; }
  .rule { height: 2px; background: currentColor; margin: 12px 0 10px; }
  .claim { opacity: .9; }
  .mark { border-radius: 50%; background: var(--gold); }
  .label--light .mark { background: var(--ink); }
  .by { margin-top: auto; font-size: 17px; }
  .brand {
    font-family: "Questrial", sans-serif; letter-spacing: .04em;
    padding: 6px 10px; margin: 6px 0 14px;
  }
  .label--dark .brand { background: var(--gold); color: var(--ink); }
  .label--light .brand { background: var(--ink); color: var(--gold); }
  .volume { margin-bottom: 16px; }

  .styling-cream { width: 230px; height: 470px; padding-top: 60px; }
  .styling-cream .product-name { font-size: 26px; }
  .styling-cream .rule { width: 140px; }
  .styling-cream .claim { font-size: 16px; }
  .styling-cream .mark { width: 40px; height: 40px; margin-top: 70px; }
  .styling-cream .brand { font-size: 26px; }
  .styling-cream .volume { font-size: 16px; }

  .hair-oil { width: 155px; height: 215px; padding-top: 16px; }
  .hair-oil .product-name { font-size: 24px; }
  .hair-oil .rule { width: 110px; height: 1px; margin: 4px 0 6px; }
  .hair-oil .claim { font-size: 12px; }
  .hair-oil .mark { width: 22px; height: 22px; margin-top: 20px; }
  .hair-oil .brand { font-size: 18px; margin-top: auto; padding: 3px 8px; margin-bottom: 8px; }
  .hair-oil .volume { font-size: 10px; margin-bottom: 10px; }

  .shampoo { width: 262px; height: 380px; padding-top: 26px; }
  .shampoo .product-name { font-size: 34px; }
  .shampoo .rule { width: 164px; margin: 10px 0 20px; }
  .shampoo .claim { font-size: 19px; }
  .shampoo .mark { width: 40px; height: 40px; margin-top: 38px; }
  .shampoo .brand { font-size: 30px; width: 160px; margin-top: auto; margin-bottom: 20px; }
  .shampoo .volume { font-size: 19px; margin-bottom: 28px; }

  .conditioner { width: 230px; height: 470px; padding-top: 50px; }
  .conditioner .product-name { font-size: 30px; }
  .conditioner .rule { width: 140px; margin: 8px 0 10px; }
  .conditioner .claim { font-size: 16px; }
  .conditioner .mark { width: 50px; height: 50px; margin-top: 60px; }
  .conditioner .brand { font-size: 24px; }
  .conditioner .volume { font-size: 16px; }

  .leave-in { width: 180px; height: 420px; padding-top: 36px; align-items: flex-start; padding-left: 18px; text-align: left; }
  .leave-in .product-name { font-size: 26px; }
  .leave-in .rule { width: 124px; margin: 8px 0 8px; }
  .leave-in .claim { font-size: 15px; }
  .leave-in .mark { width: 34px; height: 34px; margin: 70px 0 0 52px; }
  .leave-in .brand { font-size: 24px; margin-top: auto; margin-bottom: 12px; }
  .leave-in .volume { font-size: 15px; margin-left: 8px; margin-bottom: 26px; }
</style>
</head>
<body>
<main class="line-up">
  <section class="label label--dark styling-cream">
    <h2 class="product-name">styling cream</h2>
    <div class="rule"></div>
    <p class="claim">for all hair types</p>
    <span class="mark"></span>
    <p class="by">by</p>
    <p class="brand">Corvella</p>
    <p class="volume">Net.Wt. 75 ml</p>
  </section>

  <section class="label label--light hair-oil">
    <h2 class="product-name">hair oil</h2>
    <div class="rule"></div>
    <p class="claim">for all hair types</p>
    <span class="mark"></span>
    <p class="brand">Corvella</p>
    <p class="volume">Net.Wt. 30 ml</p>
  </section>

  <section class="label label--dark shampoo">
    <h2 class="product-name">shampoo</h2>
    <div class="rule"></div>
    <p class="claim">for all hair types</p>
    <span class="mark"></span>
    <p class="brand">Corvella</p>
    <p class="volume">Net.Wt. 200 ml</p>
  </section>

  <section class="label label--light conditioner">
    <h2 class="product-name">conditioner</h2>
    <div class="rule"></div>
    <p class="claim">for all hair types</p>
    <span class="mark"></span>
    <p class="by">by</p>
    <p class="brand">Corvella</p>
    <p class="volume">Net.Wt. 75 ml</p>
  </section>

  <section class="label label--dark leave-in">
    <h2 class="product-name">leave-in<br>treatments</h2>
    <div class="rule"></div>
    <p class="claim">for all hair types</p>
    <span class="mark"></span>
    <p class="brand">Corvella</p>
    <p class="volume">Net.Wt. 200 ml</p>
  </section>
</main>
</body>
</html>
```